Paraffin Wax Packaging Design for Nail and Beauty Industry

We need an attractive design for the packaging of our new product, Paraffin Wax. Our company is a wholesale beauty/nail supply company that has been selling to nail salons in the US market for 10 years. We currently sell this product that we buy from another company. Now we want to launch our own brand of Paraffin Wax.

Target Market(s)

Retail nail salons in the US market.

Industry/Entity Type

Industry

Font styles to use
Sans Serif

Colors

Designer to choose colors to be used in the design.

Requirements
Must have
• Our logo (attached).
• All information on the "Ingredient List" (attached).
• Design for Clear Packaging so product can show through.
• Design for Package Dimensions of 4.25" x 11" (110cm x 280 cm).
Nice to have
• Picture related to women's skin and or beauty.
• Contrast as in the design of product that we currently sell (attached).

```html
<!DOCTYPE html>
<html lang="en">
<head>
<meta charset="utf-8">
<title>Paraffin Wax Pouch – Flat Dieline</title>
<link href="https://fonts.googleapis.com/css2?family=Cinzel:wght@500;600&family=Crimson+Text:wght@400;600&family=Open+Sans:wght@600&display=swap" rel="stylesheet">
<style>
  :root {
    --page: #e6e6e7;
    --panel-grey: #a9a9ac;
    --magenta: #c1187c;
    --magenta-light: #e8499b;
    --pink-box: #e5569f;
    --ink: #111111;
    --band: #141414;
    --white: #ffffff;
    --fold: #5a5a5e;
    --photo-a: #e9c8b4;
    --photo-b: #c89a86;
  }
  * { box-sizing: border-box; margin: 0; padding: 0; }
  html, body { width: 1200px; height: 879px; overflow: hidden; background: var(--page); }
  .dieline {
    position: absolute; left: 282px; top: 68px;
    width: 636px; height: 742px;
    background: var(--panel-grey); overflow: hidden;
  }
  .dieline svg.shapes { position: absolute; inset: 0; }
  .photo {
    position: absolute; left: 226px; top: 198px; width: 232px; height: 306px;
    background: radial-gradient(ellipse at 55% 40%, var(--photo-a), var(--photo-b) 75%, transparent 76%);
  }
  .logo-pill {
    position: absolute; background: var(--white); border-radius: 40px;
    display: flex; align-items: center; justify-content: center;
    font-family: "Crimson Text", serif; font-weight: 600; color: #1d2a5a;
  }
  .logo-front { left: 202px; top: 86px; width: 227px; height: 78px; font-size: 34px; }
  .logo-back { left: 486px; top: 160px; width: 96px; height: 30px; font-size: 14px; }
  .back-panel {
    position: absolute; left: 462px; top: 214px; width: 144px;
    text-align: center; color: var(--ink);
  }
  .back-title { font-family: "Cinzel", serif; font-weight: 600; font-size: 19px; line-height: 1.05; }
  .back-copy {
    font-family: "Crimson Text", serif; font-weight: 600; font-size: 9.2px;
    line-height: 1.18; margin: 10px auto 0; width: 86px;
  }
  .back-copy + .back-copy { margin-top: 9px; }
  .title-band {
    position: absolute; left: 30px; top: 504px; width: 576px; height: 52px;
    background: var(--band);
    border-top: 3px solid #d8d8da; border-bottom: 3px solid #d8d8da;
    display: flex; align-items: center; justify-content: center;
    font-family: "Cinzel", serif; font-weight: 500; font-size: 30px; color: var(--white);
  }
  .front-copy { position: absolute; left: 150px; width: 336px; text-align: center; color: var(--white); }
  .compat { top: 565px; font-family: "Open Sans", sans-serif; font-weight: 600; font-size: 11.2px; line-height: 1.4; }
  .benefit {
    top: 604px; left: 218px; width: 201px; height: 31px; background: var(--pink-box);
    font-family: "Crimson Text", serif; font-size: 10.4px; line-height: 1.3; padding-top: 2px;
  }
  .net { top: 650px; font-family: "Open Sans", sans-serif; font-weight: 600; font-size: 7.6px; }
</style>
</head>
<body>
  <main class="dieline">
    <svg class="shapes" width="636" height="742" viewBox="0 0 636 742">
      <path d="M138 0 L268 0 C205 70 205 160 270 240 C330 320 440 380 468 450 L520 742 L30 742 L30 690 C90 600 205 450 205 300 C205 180 158 80 138 0 Z" fill="var(--magenta)"/>
      <path d="M205 300 C205 450 90 600 30 690 L30 742 L52 742 C110 620 220 470 222 300 C222 180 176 80 150 0 L138 0 C158 80 205 180 205 300 Z" fill="var(--white)"/>
      <path d="M270 240 C330 320 440 380 468 450 L520 742 L540 742 L486 440 C460 370 350 310 290 240 C240 170 245 70 300 0 L268 0 C205 70 205 160 270 240 Z" fill="var(--white)" opacity="0.9"/>
      <path d="M468 560 C500 620 505 690 500 742 L528 742 C534 680 520 610 488 560 Z" fill="var(--magenta-light)"/>
      <path d="M60 742 C110 640 160 590 180 560 L200 560 C170 610 120 680 90 742 Z" fill="var(--magenta-light)"/>
      <g stroke="var(--fold)" stroke-width="1" stroke-dasharray="5 4" fill="none">
        <line x1="32" y1="0" x2="32" y2="742"/>
        <line x1="175" y1="0" x2="175" y2="742"/>
        <line x1="462" y1="0" x2="462" y2="742"/>
        <line x1="606" y1="0" x2="606" y2="742"/>
        <line x1="0" y1="31" x2="636" y2="31"/>
        <line x1="0" y1="710" x2="636" y2="710"/>
      </g>
    </svg>

    <div class="photo" role="img" aria-label="Beauty portrait of a woman with a towel wrapped on her head"></div>

    <div class="logo-pill logo-front">By Velora</div>
    <div class="logo-pill logo-back">By Velora</div>

    <section class="back-panel">
      <h2 class="back-title">PARAFFIN<br>WAX</h2>
      <p class="back-copy">INGREDIENTS:<br>Paraffin waxes and Hydrocarbon waxes, Petrolatum, Paraffin oils, Apricot kernel oil, Fragrance D &amp; C dyes.</p>
      <p class="back-copy">CAUTION:<br>Paraffin is flammable. Do not use near open flame or an unprotected resistance heater.</p>
    </section>

    <h1 class="title-band">PARAFFIN WAX</h1>
    <p class="front-copy compat">COMPATIBLE FOR USE WITH MOST<br>WAX PARAFFIN HEAT THERAPY UNITS.</p>
    <p class="front-copy benefit">Deeply Moisturizes the Skin Restoring a<br>Healthier Look and Feel to Skin.</p>
    <p class="front-copy net">NET WT. 1 LB. (450 G.)</p>
  </main>
</body>
</html>
```